new roofing company card

New primary business card for roofing company.

Industry/Entity Type

Residential roofing/Specializing in Asphalt and Standing seam metal roofing

Contact Information for Business Card

Phone number is: 484 672 1058 Email: support@fennridgeroofworks.com website: www.fennridgeroofworks.com

Colors
EB3D1F
EC4F4E
F09395
F8D3D4
FCEDEE

```html
<!DOCTYPE html>
<html lang="en">
<head>
<meta charset="utf-8">
<title>Fennridge Roofworks – Business Card</title>
<link href="https://fonts.googleapis.com/css2?family=Montserrat:wght@400;500;700&display=swap" rel="stylesheet">
<style>
  :root {
    --bg: #1f1f1f;
    --card: #ffffff;
    --ink: #2b2b2b;
    --red: #c8281f;
    --red-soft: #EC4F4E;
  }
  * { margin: 0; padding: 0; box-sizing: border-box; }
  html, body { width: 1200px; height: 874px; overflow: hidden; }
  body { background: var(--bg); font-family: "Montserrat", sans-serif; position: relative; }

  .card {
    position: absolute;
    width: 580px;
    height: 332px;
    background: var(--card);
    border-radius: 22px;
    overflow: hidden;
  }
  .card--front { left: 470px; top: 70px; display: flex; align-items: center; justify-content: center; }
  .card--back { left: 150px; top: 470px; display: flex; align-items: center; padding: 0 28px; }

  .brand { display: flex; align-items: center; gap: 16px; color: var(--ink); }
  .brand__square { width: 22px; height: 22px; background: var(--red); flex: none; }
  .brand__name { font-weight: 700; line-height: 1.05; text-transform: uppercase; letter-spacing: 1px; }
  .card--front .brand__name { font-size: 44px; }
  .card--back .brand { width: 196px; gap: 10px; flex: none; }
  .card--back .brand__name { font-size: 22px; }
  .card--back .brand__square { width: 14px; height: 14px; }

  .divider { width: 2px; height: 190px; background: var(--red); margin: 0 20px 0 14px; flex: none; }

  .contact { color: var(--ink); min-width: 0; }
  .contact__name { color: var(--red); font-weight: 700; font-size: 24px; letter-spacing: 0.5px; white-space: nowrap; }
  .contact__title { font-size: 14px; margin-top: 4px; }
  .contact__list { list-style: none; margin-top: 24px; }
  .contact__list li { display: flex; align-items: center; gap: 8px; font-size: 13.5px; margin-bottom: 7px; white-space: nowrap; }
  .contact__list svg { width: 13px; height: 13px; flex: none; fill: var(--red); }
</style>
</head>
<body>
  <section class="card card--front">
    <div class="brand">
      <span class="brand__square"></span>
      <span class="brand__name">Fennridge<br>Roofworks</span>
    </div>
  </section>

  <section class="card card--back">
    <div class="brand">
      <span class="brand__square"></span>
      <span class="brand__name">Fennridge<br>Roofworks</span>
    </div>
    <span class="divider"></span>
    <div class="contact">
      <h1 class="contact__name">DANIEL HARLOW</h1>
      <p class="contact__title">Managing Director</p>
      <ul class="contact__list">
        <li>
          <svg viewBox="0 0 24 24" aria-hidden="true"><path d="M6.6 10.8a15.1 15.1 0 0 0 6.6 6.6l2.2-2.2a1 1 0 0 1 1-.25 11.4 11.4 0 0 0 3.6.57 1 1 0 0 1 1 1V20a1 1 0 0 1-1 1A17 17 0 0 1 3 4a1 1 0 0 1 1-1h3.5a1 1 0 0 1 1 1c0 1.25.2 2.45.57 3.57a1 1 0 0 1-.25 1z"/></svg>
          484 672 1058
        </li>
        <li>
          <svg viewBox="0 0 24 24" aria-hidden="true"><path d="M2 5h20v14H2z M2 5l10 8 10-8" stroke="#fff" stroke-width="1.5"/></svg>
          support@fennridgeroofworks.com
        </li>
        <li>
          <svg viewBox="0 0 24 24" aria-hidden="true"><circle cx="12" cy="12" r="10"/><path d="M2 12h20M12 2c3 3 3 17 0 20M12 2c-3 3-3 17 0 20" stroke="#fff" stroke-width="1.3" fill="none"/></svg>
          www.fennridgeroofworks.com
        </li>
      </ul>
    </div>
  </section>
</body>
</html>
```